A QUIET AMBER PRIMER ON RANKS

subtitle: AN INTRO TO SEARCH ENGINE OPTIMIZATION
background: white
dimensions: 1562x2500

Target Market(s)

Marketing professionals

Industry/Entity Type

Digital Marketing

Font styles to use
Sans Serif

Colors
ffffff
1b1b1b
3176b5

Requirements
Should not have
• Images or graphics

```html
<!DOCTYPE html>
<html lang="en">
<head>
<meta charset="utf-8">
<title>A Quiet Amber Primer on Ranks</title>
<link rel="stylesheet" href="https://fonts.googleapis.com/css2?family=Oswald:wght@500&family=Open+Sans:wght@400;700&display=swap">
<style>
  :root {
    --paper-light: #eceeef;
    --paper-mid: #dedfe0;
    --paper-warm: #c9bfbf;
    --ink: #1b1b1b;
    --ink-soft: #555555;
    --brand-blue: #3176b5;
    --white: #ffffff;
    --title-white: #f7f7f7;
  }
  html, body {
    margin: 0;
    padding: 0;
    width: 750px;
    height: 1200px;
    overflow: hidden;
    background: var(--paper-mid);
  }
  .cover {
    display: block;
    width: 750px;
    height: 1200px;
  }
  .title-small {
    font-family: "Oswald", "Arial Narrow", sans-serif;
    font-weight: 500;
    fill: var(--brand-blue);
  }
  .title-large {
    font-family: "Oswald", "Arial Narrow", sans-serif;
    font-weight: 500;
    fill: var(--title-white);
  }
  .title-accent {
    font-family: "Open Sans", Arial, sans-serif;
    font-weight: 700;
    fill: var(--brand-blue);
  }
  .subtitle {
    font-family: "Open Sans", Arial, sans-serif;
    font-weight: 400;
    fill: var(--ink-soft);
    letter-spacing: 2px;
  }
  .author {
    font-family: "Open Sans", Arial, sans-serif;
    font-weight: 400;
    fill: var(--white);
  }
</style>
</head>
<body>
<svg class="cover" viewBox="0 0 750 1200" xmlns="http://www.w3.org/2000/svg" aria-labelledby="cover-title">
  <title id="cover-title">A Quiet Amber Primer on Ranks — An introduction to SEO</title>
  <defs>
    <linearGradient id="paper-base" x1="0" y1="0" x2="0.3" y2="1">
      <stop offset="0" stop-color="#f1f2f3"/>
      <stop offset="0.55" stop-color="#dcdddf"/>
      <stop offset="1" stop-color="#cfcac9"/>
    </linearGradient>
    <radialGradient id="paper-glow" cx="0.78" cy="0.08" r="0.6">
      <stop offset="0" stop-color="#ffffff" stop-opacity="0.8"/>
      <stop offset="1" stop-color="#ffffff" stop-opacity="0"/>
    </radialGradient>
    <radialGradient id="paper-warmth" cx="0.1" cy="0.98" r="0.55">
      <stop offset="0" stop-color="#b9a9a8" stop-opacity="0.7"/>
      <stop offset="1" stop-color="#b9a9a8" stop-opacity="0"/>
    </radialGradient>
    <filter id="lift-shadow" x="-10%" y="-10%" width="120%" height="130%">
      <feDropShadow dx="3" dy="4" stdDeviation="3" flood-color="#000000" flood-opacity="0.45"/>
    </filter>
    <filter id="soft-shadow" x="-10%" y="-10%" width="120%" height="130%">
      <feDropShadow dx="2" dy="3" stdDeviation="2" flood-color="#000000" flood-opacity="0.35"/>
    </filter>
  </defs>

  <g class="background">
    <rect width="750" height="1200" fill="url(#paper-base)"/>
    <rect width="750" height="1200" fill="url(#paper-glow)"/>
    <rect width="750" height="1200" fill="url(#paper-warmth)"/>
  </g>

  <g class="title" aria-label="A Quiet Amber Primer on Ranks">
    <text class="title-small" x="205" y="170" font-size="72" textLength="340" lengthAdjust="spacingAndGlyphs">A QUIET</text>
    <text class="title-large" x="108" y="410" font-size="290" textLength="552" lengthAdjust="spacingAndGlyphs" filter="url(#lift-shadow)">AMBER</text>
    <text class="title-large" x="112" y="650" font-size="290" textLength="520" lengthAdjust="spacingAndGlyphs" filter="url(#lift-shadow)">PRIMER</text>
    <text class="title-small" x="357" y="725" font-size="60" textLength="56" lengthAdjust="spacingAndGlyphs">ON</text>
    <text class="title-accent" x="145" y="960" font-size="280" textLength="500" lengthAdjust="spacingAndGlyphs" filter="url(#soft-shadow)">RANKS</text>
  </g>

  <text class="subtitle" x="110" y="1092" font-size="36" textLength="530">An introduction to SEO</text>
  <text class="author" x="100" y="1178" font-size="78" textLength="560" filter="url(#soft-shadow)">Author´s name</text>
</svg>
</body>
</html>
```